Business card for our large format printing and installation business

We want a professional looking business card for our business. We manufacture and install Signs.

On the back of the card add this info
Large Format Graphics Printing & Installations, Event Graphics, Banners, Posters, Vehicle Fleet Graphics, Boat Wraps, Wall Murals, Decals,Displays,Signs,Plaques,Digital Signs

On the Front of the card add the Tallowfern Signs logo, plus On the back of the card add the Orange Tallowfern Wraps logo. The 2 vector logos are attached to the design brief.

Target Market(s)

Local business owners

Contact Information for Business Card

Colors
f37122
f68d4e
f9ba93

Requirements
Must have
• On the Front of the card add the Tallowfern Signs logo, plus On the back of the card add the Orange Tallowfern Wraps logo. The 2 vector logos are attached to the design brief.

```html
<!DOCTYPE html>
<html lang="en">
<head>
<meta charset="utf-8">
<title>Tallowfern Signs – Business Card</title>
<link href="https://fonts.googleapis.com/css2?family=Montserrat:ital,wght@0,400;0,500;0,700;1,400&display=swap" rel="stylesheet">
<style>
  :root {
    --orange: #f37122;
    --orange-mid: #f68d4e;
    --orange-light: #f9ba93;
    --logo-gold: #fbb02a;
    --ink: #111111;
    --charcoal: #3a3a3a;
    --black: #000000;
    --white: #ffffff;
    --label: #222222;
  }
  * { margin: 0; padding: 0; box-sizing: border-box; }
  html, body {
    width: 1200px; height: 1013px; overflow: hidden;
    background: var(--white);
    font-family: "Montserrat", Arial, sans-serif;
  }
  .canvas { position: relative; width: 1200px; height: 1013px; }
  .side-label {
    position: absolute; top: 55px; width: 490px; text-align: center;
    font-size: 34px; font-weight: 400; color: var(--label); letter-spacing: 0.5px;
  }
  .side-label--front { left: 50px; }
  .side-label--back { left: 645px; }

  .card { position: absolute; top: 112px; width: 490px; height: 840px; overflow: hidden; }
  .card--front { left: 58px; background: var(--white); }
  .card--back {
    left: 655px;
    background: radial-gradient(ellipse 70% 55% at 50% 48%, #5a5a5a 0%, #2c2c2c 45%, var(--black) 85%);
  }

  .front-header { position: absolute; left: 0; top: 0; width: 490px; height: 250px; }
  .front-header__panel {
    position: absolute; inset: 0 0 20px 0;
    background: radial-gradient(ellipse 80% 90% at 50% 60%, #333 0%, #161616 60%, var(--black) 100%);
  }
  .front-footer {
    position: absolute; left: 0; bottom: 0; width: 490px; height: 35px;
    background: linear-gradient(90deg, #151515, var(--charcoal) 55%, #151515);
  }

  .wordmark {
    position: absolute; left: 0; width: 100%; text-align: center;
    font-weight: 700; color: var(--logo-gold); line-height: 1;
  }
  .wordmark--front { top: 92px; font-size: 46px; }
  .wordmark--back { top: 392px; font-size: 46px; }

  .contact { position: absolute; left: 0; top: 0; width: 490px; }
  .person__name {
    position: absolute; left: 57px; top: 272px;
    font-size: 40px; font-weight: 700; color: var(--ink); white-space: nowrap;
  }
  .person__title {
    position: absolute; left: 57px; top: 322px;
    font-size: 33px; font-style: italic; font-weight: 400; color: var(--ink);
  }
  .info-row { position: absolute; left: 57px; display: flex; align-items: flex-start; }
  .info-row__icon { width: 32px; flex: none; margin-right: 17px; }
  .info-row__text { font-size: 24px; font-weight: 400; color: var(--ink); line-height: 33px; white-space: nowrap; }
  .row--email { top: 404px; }
  .row--address { top: 453px; }
  .row--office { top: 576px; }
  .row--direct { top: 628px; }
  .phone-label--office { font-weight: 700; font-size: 25px; }
  .phone-number--office { font-weight: 700; font-size: 34px; }
  .phone-label--direct { font-size: 25px; }
  .phone-number--direct { font-size: 32px; }

  .web-address {
    position: absolute; left: 0; width: 100%; text-align: center;
    font-weight: 700; font-size: 29px; letter-spacing: 0.3px;
  }
  .web-address--front { top: 723px; color: var(--ink); }
  .web-address--back { top: 758px; color: var(--white); }
</style>
</head>
<body>
<div class="canvas">
  <div class="side-label side-label--front">FRONT</div>
  <div class="side-label side-label--back">BACK</div>

  <section class="card card--front">
    <div class="front-header">
      <div class="front-header__panel"></div>
      <svg width="490" height="250" viewBox="0 0 490 250" style="position:absolute;left:0;top:0">
        <path d="M0 230 L490 230 L490 252 Q245 252 0 234 Z" fill="#dddddd"/>
        <path d="M0 230 L490 230 L490 248 Q245 248 0 240 Z" fill="var(--orange)"/>
      </svg>
      <div class="wordmark wordmark--front">Tallowfern Signs</div>
    </div>

    <div class="contact">
      <div class="person__name">Marcus Delgado</div>
      <div class="person__title">CEO</div>

      <div class="info-row row--email">
        <svg class="info-row__icon" width="32" height="24" viewBox="0 0 32 24" style="margin-top:6px">
          <rect x="1" y="3" width="30" height="18" fill="var(--orange)"/>
          <path d="M1 3 L16 14 L31 3" fill="none" stroke="var(--white)" stroke-width="2"/>
          <path d="M1 21 L12 11 M31 21 L20 11" stroke="var(--white)" stroke-width="1.5"/>
        </svg>
        <span class="info-row__text">marcus@tallowfern.net</span>
      </div>

      <div class="info-row row--address">
        <svg class="info-row__icon" width="32" height="34" viewBox="0 0 32 34">
          <path d="M16 1 C8 1 3 7 3 13 C3 21 16 33 16 33 C16 33 29 21 29 13 C29 7 24 1 16 1 Z" fill="var(--orange)"/>
          <circle cx="16" cy="13" r="5" fill="var(--white)"/>
        </svg>
        <span class="info-row__text">1840 Harbor View Drive #7<br>Coral Bay, FL 33120</span>
      </div>

      <div class="info-row row--office">
        <svg class="info-row__icon" width="32" height="28" viewBox="0 0 32 28" style="margin-top:8px">
          <path d="M2 9 Q16 -1 30 9 L30 13 L23 13 L23 9 Q16 7 9 9 L9 13 L2 13 Z" fill="var(--orange)"/>
          <path d="M6 15 L26 15 L29 26 L3 26 Z" fill="var(--orange)"/>
          <circle cx="16" cy="20" r="3.5" fill="var(--white)"/>
        </svg>
        <span class="info-row__text"><span class="phone-label--office">Office: </span><span class="phone-number--office">305-555-0148</span></span>
      </div>

      <div class="info-row row--direct">
        <svg class="info-row__icon" width="32" height="38" viewBox="0 0 32 38">
          <rect x="6" y="2" width="20" height="34" rx="3" fill="none" stroke="var(--orange)" stroke-width="2.5"/>
          <line x1="13" y1="6" x2="19" y2="6" stroke="var(--orange)" stroke-width="2"/>
          <circle cx="16" cy="31" r="1.8" fill="var(--orange)"/>
        </svg>
        <span class="info-row__text"><span class="phone-label--direct">Direct: </span><span class="phone-number--direct">305-555-0192</span></span>
      </div>
    </div>

    <div class="web-address web-address--front">www.Tallowfernwraps.com</div>
    <div class="front-footer"></div>
  </section>

  <section class="card card--back">
    <div class="wordmark wordmark--back">Tallowfern Signs</div>
    <div class="web-address web-address--back">www.Tallowfernwraps.com</div>
  </section>
</div>
</body>
</html>
```